Dane Morrow films- wedding and event films company website. DESKTOP AND MOBILE

We need a website for a high-end wedding and event film production company. Looking for a very modern and elegant design. my old website is www.danemorrowfilms.example

I like the "white/black/rose gold" color scheme of my logo.

really looking for a sleek modern design the breaths professional and artistic.

Target Market(s)

wedding and event films.

Industry/Entity Type

Film Production

Number of Pages Required

5+ page

Colors

Designer to choose colors to be used in the design.

Requirements
Must have
• website name will be www.danemorrowfilms.example
• tagline is "CINEMATIC STORIES ABOUT YOU"
• sections: HOME, CONTACT, ABOUT, FILMS, BLOG
• You can see my old website at danemorrowfilms.example
• Website about section:
• Dane Morrow Films was Established with the basis of truly cinematic and artistic films in mind. Dane and his team routinely travel the globe documenting weddings and events for high profile clients and discerning couples. Dane was born and raised in Maui Hawaii and has a unique approach to his films that embody the essence of a Hollywood film. Dane has spent the last 10 years traveling the world documenting corporate events and weddings with multiple Award winning production companies. In 2017 Dane decided to establish his own brand “Dane Morrow films” that will take everything he has learned with his past experiences and push it to the next level. Aside from his personal achievements, Dane is extremely passionate about his craft and always looks forward to handcrafting beautiful wedding/event films for his clients. The style of work is non-traditional and the day of filming is extremely unobtrusive (as we are looking for natural-candid/ raw emotions).
• If you are looking for the best price in town, we are probably not the best option, but if you’re looking for the best quality and peace of mind on your wedding day, then you’re in the right place. Dane Morrow Films is a boutique studio that only accepts a limited number of assignments per year. Inquire early to ensure availability.
• LINKS TO VIMEO VIDEOS THAT WILL BE IN THE "FILMS' SECTION.
• BRENT FILM TRAILER - https://clipvault.example/508114362
• BRENT FEATURE FILM - https://clipvault.example/617392048
• JUNE AND ROB'S WEDDING - https://clipvault.example/724958160
• DRONE DEMO REEL - https://clipvault.example/841576203
• WEDDING INDUSTRY EVENT PARTY - https://clipvault.example/962304817/a8d3e7b21c
• images that you can use on site are here: https://brigittolsenimages.proofbox.example/gallery/nora&felix/
• password is: meadow

```html
<!DOCTYPE html>
<html lang="en">
<head>
<meta charset="utf-8">
<title>Dane Morrow Films</title>
<link rel="stylesheet" href="https://fonts.googleapis.com/css2?family=Montserrat:wght@400;500;700&family=Roboto:wght@400;500&display=swap">
<style>
:root{
  --white:#ffffff;
  --ink:#222222;
  --muted:#8a8a8a;
  --quote-text:#6b6b6b;
  --rose-gold:#c98a5e;
  --accent:#e0883a;
  --band:#e8e9ec;
  --footer:#2b2b2b;
}
*{margin:0;padding:0;box-sizing:border-box}
html,body{width:942px;height:1200px;overflow:hidden;background:var(--white)}
body{position:relative;font-family:"Roboto",Arial,sans-serif;color:var(--ink)}
.sidebar{position:absolute;left:0;top:0;width:250px;height:413px}
.brand{position:absolute;left:88px;top:48px;text-align:center;width:96px}
.brand-name{font-family:"Montserrat",sans-serif;font-size:10px;font-weight:500;letter-spacing:1.2px;color:var(--ink);display:block;white-space:nowrap}
.brand-sub{font-family:"Montserrat",sans-serif;font-size:5px;font-weight:500;letter-spacing:2px;color:var(--ink);display:block;margin-top:2px}
.brand-dot{position:absolute;left:40px;top:-22px;width:14px;height:14px;background:var(--rose-gold)}
.side-nav{position:absolute;left:91px;top:113px;list-style:none}
.side-nav li{height:35.2px;font-size:7.5px;letter-spacing:.3px}
.hero{position:absolute;left:250px;top:0;width:692px;height:413px;background:linear-gradient(120deg,#8e8b8c 0%,#b08f86 35%,#9c7566 60%,#6e5444 100%)}
.hero-title{position:absolute;left:26px;top:137px;font-family:"Montserrat",sans-serif;font-weight:700;font-size:19.5px;line-height:23.5px;letter-spacing:.5px;color:var(--white)}
.hero-lead{position:absolute;left:26px;top:192px;font-family:"Montserrat",sans-serif;font-size:7.4px;line-height:12px;color:var(--white)}
.hero-btn{position:absolute;left:23px;top:253px;width:79px;height:26px;border:1.3px solid var(--white);border-radius:13px;color:var(--white);font-size:7px;text-align:center;line-height:23px}
.hero-dots{position:absolute;left:225px;top:385px;display:flex;gap:7px}
.hero-dots span{width:6px;height:6px;border-radius:50%;background:rgba(255,255,255,.45)}
.hero-dots span.active{background:var(--white)}
.hero-arrows{position:absolute;left:548px;top:382px}
.about-title{position:absolute;left:88px;top:544px;font-size:15px;font-weight:400;letter-spacing:.3px}
.about-text{position:absolute;left:88px;top:580px;width:332px;font-size:6.9px;line-height:14.7px;color:var(--muted)}
.know-more{position:absolute;left:92px;top:690px;font-size:8.5px;font-weight:500;color:var(--accent);display:flex;align-items:center;gap:13px}
.portrait{position:absolute;left:515px;top:475px;width:337px;height:299px;background:linear-gradient(135deg,#bdbdbd 0%,#8c8c8c 50%,#3a3a3a 100%)}
.testimonial{position:absolute;left:0;top:843px;width:942px;height:262px;background:var(--band);text-align:center}
.quote-mark{position:absolute;left:464px;top:62px}
.quote-text{position:absolute;left:0;right:0;top:96px;font-size:14.5px;line-height:23.5px;color:var(--quote-text)}
.quote-name{position:absolute;left:0;right:0;top:174px;font-size:14px;color:var(--ink)}
.footer{position:absolute;left:0;top:1105px;width:942px;height:95px;background:var(--footer);color:var(--white)}
.footer-nav{position:absolute;top:30px;left:0;list-style:none;font-size:7.5px;letter-spacing:.3px}
.footer-nav li{position:absolute;white-space:nowrap}
.contact{position:absolute;left:688px;font-size:10px;display:flex;align-items:center;gap:9px;white-space:nowrap}
</style>
</head>
<body>
<aside class="sidebar">
  <div class="brand">
    <span class="brand-dot"></span>
    <span class="brand-name">DANE MORROW</span>
    <span class="brand-sub">FILMS</span>
  </div>
  <ul class="side-nav">
    <li>HOME</li><li>CONTACT</li><li>ABOUT</li><li>FILMS</li><li>BLOG</li>
  </ul>
</aside>

<section class="hero" role="img" aria-label="Close-up of a groom placing a gold wedding ring on the bride's finger">
  <h1 class="hero-title">CINEMATIC STORIES<br>ABOUT YOU</h1>
  <p class="hero-lead">Lorem ipsum dolor sit amet, consectetur adipiscing elit.<br>Nunc mollis tellus eu ipsum faucibus.</p>
  <div class="hero-btn">view more</div>
  <div class="hero-dots"><span></span><span class="active"></span><span></span></div>
  <svg class="hero-arrows" width="56" height="12" viewBox="0 0 56 12" fill="none" stroke="#fff" stroke-width="1.3">
    <path d="M2 6H22M2 6l4-3M2 6l4 3"/>
    <path d="M34 6H54M54 6l-4-3M54 6l-4 3"/>
  </svg>
</section>

<h2 class="about-title">ABOUT US</h2>
<p class="about-text">At Dane Morrow Films we specialize in offering the finest in wedding and corporate cinema­tography. We offer a very modern and creative style for capturing your special moments with a beautiful and cinematic approach that enables up to produce the highest quality of films. Dane and his hand selected team have over 10 years of experience, and they strive to make the best films in the industry. We pride ourselves on remaining attentive...</p>
<div class="know-more">Know more
  <svg width="22" height="6" viewBox="0 0 22 6" fill="none" stroke="#e0883a" stroke-width="1"><path d="M0 3H21M21 3l-3-2M21 3l-3 2"/></svg>
</div>
<div class="portrait" role="img" aria-label="Black and white portrait of the filmmaker in a dark shirt"></div>

<section class="testimonial">
  <svg class="quote-mark" width="20" height="13" viewBox="0 0 20 13" fill="#111">
    <circle cx="4.5" cy="8.5" r="4.5"/><path d="M1 8C1 4 3 1 7 0L7.5 1.5C5 2.5 4 4.5 4 7Z"/>
    <circle cx="15.5" cy="8.5" r="4.5"/><path d="M12 8C12 4 14 1 18 0L18.5 1.5C16 2.5 15 4.5 15 7Z"/>
  </svg>
  <p class="quote-text">Dane really is one of the best film makers in Hawaii,<br>great work Dane! We loved the film!</p>
  <p class="quote-name">— Lea Hanson</p>
</section>

<footer class="footer">
  <ul class="footer-nav">
    <li style="left:113px">HOME</li>
    <li style="left:180px">CONTACT</li>
    <li style="left:259px">ABOUT</li>
    <li style="left:329px">FILMS</li>
    <li style="left:395px">BLOG</li>
  </ul>
  <div class="contact" style="top:28px">
    <svg width="12" height="9" viewBox="0 0 12 9" fill="none" stroke="#fff" stroke-width="1"><rect x=".5" y=".5" width="11" height="8"/><path d="M.5 .5L6 5l5.5-4.5"/></svg>
    dane@danemorrowfilms.example
  </div>
  <div class="contact" style="top:53px;left:692px">
    <svg width="10" height="10" viewBox="0 0 10 10" fill="#fff"><path d="M2 0L4 2.5 3 4C3.8 5.6 4.4 6.2 6 7L7.5 6 10 8 8.5 10C4 9.5.5 6 0 1.5Z"/></svg>
    (808) 555-0147
  </div>
</footer>
</body>
</html>
```